Local Horticulturalist needs Business card design

Meridel Horticulture would like to update our existing business card and utilize our new logo (design attached)....we specialize in getting the best out of our customers yard with professional maintenance programs, expert pruning and hedging and garden restorations.
Utilizing colors from attached logo I would like a design that implies professionalism and if possible our businesses love of restoration through plants.
I also sometimes write down for my customers a start date and price on the back of my current card
Target Market(s)
Home owners
Contractors
Industry/Entity Type
Gardener
Contact Information for Business Card
Gareth Volkstrom | Horticulturalist
ph: 0438275946
meridelhort@fernmail.example
www.meridelhorticulture.example.au
Requirements
Must have
- crucial information easy to read
- incorporate current logo
- Horticulturalist listed preferably near name
Nice to have
- currently I write a job start date and price on the back of my current card so something that integrates this would be beneficial
Should not have
- be pretty or flowerey
- be too white or basic

```html
<!DOCTYPE html>
<html lang="en">
<head>
<meta charset="utf-8">
<title>Meridel Horticulture – Business Card</title>
<link rel="stylesheet" href="https://fonts.googleapis.com/css2?family=Open+Sans:wght@400;600;700&display=swap">
<style>
  :root {
    --leaf-green: #7cc242;
    --soil-brown: #6b5d4d;
    --sand: #d8d0c3;
    --spring: #c6eb96;
    --paper: #ffffff;
    --backdrop: #eceae5;
  }
  * { box-sizing: border-box; margin: 0; padding: 0; }
  html, body { width: 1200px; height: 1000px; overflow: hidden; }
  body {
    background: var(--backdrop);
    font-family: "Open Sans", Arial, sans-serif;
    color: var(--soil-brown);
    display: flex;
    flex-direction: column;
    align-items: center;
    justify-content: center;
    gap: 40px;
  }
  .card {
    position: relative;
    width: 760px;
    height: 440px;
    background: var(--paper);
    box-shadow: 0 6px 18px rgba(0,0,0,0.18);
    overflow: hidden;
  }
  .card-art {
    position: absolute;
    top: 0; right: 0; bottom: 0;
    width: 62%;
    background:
      linear-gradient(90deg, rgba(255,255,255,1) 0%, rgba(255,255,255,0.55) 35%, rgba(255,255,255,0) 70%),
      linear-gradient(170deg, var(--sand) 0%, #dfe3cf 55%, var(--spring) 100%);
  }
  .brand { position: absolute; display: flex; align-items: center; gap: 12px; }
  .brand-dot { width: 46px; height: 46px; border-radius: 50%; background: var(--leaf-green); flex: none; }
  .brand-name { font-weight: 700; font-size: 32px; line-height: 1; color: var(--leaf-green); letter-spacing: -0.3px; }
  .brand-tagline { font-size: 14px; letter-spacing: 1.2px; color: var(--soil-brown); margin-top: 4px; }
  .front .brand { left: 40px; top: 40px; }
  .person { position: absolute; left: 44px; top: 132px; }
  .person-name { font-weight: 700; font-size: 24px; }
  .person-role { font-size: 22px; }
  .contacts { position: absolute; left: 360px; top: 250px; font-size: 19px; display: flex; flex-direction: column; gap: 14px; }
  .contact { display: flex; align-items: center; gap: 14px; }
  .contact svg { width: 22px; height: 22px; flex: none; }
  .contact-web { margin-left: -40px; }
  .back .brand { left: 180px; top: 110px; }
  .write-line {
    position: absolute; left: 40px; width: 520px;
    border-top: 2px dotted var(--soil-brown);
  }
  .write-line.first { top: 290px; }
  .write-line.second { top: 370px; }
</style>
</head>
<body>

<section class="card front" aria-label="Business card front">
  <div class="card-art" role="img" aria-label="Decorative background area in soft beige and green tones"></div>

  <div class="brand">
    <span class="brand-dot"></span>
    <div>
      <div class="brand-name">Meridel Horticulture</div>
      <div class="brand-tagline">Garden Restorations &amp; Maintenance</div>
    </div>
  </div>

  <div class="person">
    <div class="person-name">Gareth Volkstrom</div>
    <div class="person-role">Horticulturalist</div>
  </div>

  <div class="contacts">
    <div class="contact">
      <svg viewBox="0 0 24 24" aria-hidden="true"><path d="M6.6 10.8a15 15 0 0 0 6.6 6.6l2.2-2.2a1 1 0 0 1 1-.25 11.4 11.4 0 0 0 3.6.57 1 1 0 0 1 1 1V20a1 1 0 0 1-1 1A17 17 0 0 1 3 4a1 1 0 0 1 1-1h3.5a1 1 0 0 1 1 1c0 1.25.2 2.45.57 3.57a1 1 0 0 1-.25 1z" fill="#6b5d4d"/></svg>
      <span>0438275946</span>
    </div>
    <div class="contact">
      <svg viewBox="0 0 24 24" aria-hidden="true"><rect x="2.5" y="5" width="19" height="14" fill="none" stroke="#6b5d4d" stroke-width="1.8"/><path d="M2.5 5 12 13l9.5-8" fill="none" stroke="#6b5d4d" stroke-width="1.8"/></svg>
      <span>meridelhort@fernmail.example</span>
    </div>
    <div class="contact contact-web">
      <span>www.meridelhorticulture.example.au</span>
    </div>
  </div>
</section>

<section class="card back" aria-label="Business card back">
  <div class="card-art" role="img" aria-label="Decorative background area in soft beige and green tones"></div>

  <div class="brand">
    <span class="brand-dot"></span>
    <div>
      <div class="brand-name">Meridel Horticulture</div>
      <div class="brand-tagline">Garden Restorations &amp; Maintenance</div>
    </div>
  </div>

  <div class="write-line first"></div>
  <div class="write-line second"></div>
</section>

</body>
</html>
```